Electrical contracting business specialising in smoke detector installation needs flyer design

i need a flyer design made up highlighting the fact that the Qld legislation is changing on smoke detectors in homes for everyones safety. I am an electrical contractor ( Tandrell Electrical) specialising in smoke detector installation to comply with the new Qld legislation. Some of the wording that can be used-
When you sleep, your sense of smell also sleeps. If a fire starts, toxic fumes canovercome you. Photoelectric smoke alarms see smoke and will alert you early, so you can escape. With interconnected alarms, you will be alerted no matter where you are, or where the fire starts.
New legislation specifies the type, positioning and interconnectedness of alarms, which are critical factors for an early warning and a quick escape.
To give your family the best chance of surviving a house fire, update your smoke alarms to match the new legislation as soon as you can. Call ME on 0418362957

Target Market(s)

Body Corporates , people selling and renting their properties

Industry/Entity Type

Electrician

Colors

Designer to choose colors to be used in the design.

Requirements
Must have
• Safety aspect.

```html
<!DOCTYPE html>
<html lang="en">
<head>
<meta charset="utf-8">
<title>Tandrell Electrical – Smoke Alarm Legislation</title>
<link href="https://fonts.googleapis.com/css2?family=Open+Sans:wght@400;600;700;800&display=swap" rel="stylesheet">
<style>
  :root {
    --gold: #c89a57;
    --gold-text: #c8964f;
    --charcoal: #3a3a3c;
    --charcoal-deep: #2f2f31;
    --photo-light: #8c8c8e;
    --photo-dark: #5a5a5c;
    --white: #ffffff;
    --ink: #333335;
  }
  * { box-sizing: border-box; margin: 0; padding: 0; }
  html, body { width: 848px; height: 1200px; overflow: hidden; background: var(--white); }
  body { font-family: "Open Sans", Arial, sans-serif; color: var(--white); }
  .flyer { position: relative; width: 848px; height: 1200px; }

  .band-title {
    position: absolute; left: 0; width: 848px;
    background: var(--gold);
    display: flex; align-items: center; justify-content: center;
    text-align: center; font-weight: 700; text-transform: uppercase;
    font-size: 37px; line-height: 1.08; color: var(--white);
  }
  .band-title.top { top: 0; height: 120px; }
  .band-title.middle { top: 558px; height: 122px; }

  .rule { position: absolute; top: 120px; left: 0; width: 848px; height: 18px; background: var(--charcoal); }

  .date-bar { position: absolute; top: 138px; left: 0; width: 848px; height: 36px; background: var(--white); }
  .date-bar h2 { position: absolute; top: 2px; font-size: 22px; font-weight: 700; color: var(--gold-text); }
  .date-bar .left { left: 33px; }
  .date-bar .right { left: 381px; }

  .panel { position: absolute; left: 0; width: 848px; background: var(--charcoal); font-size: 15px; line-height: 1.15; }
  .panel.rules { top: 174px; height: 384px; }
  .panel.locations { top: 680px; height: 270px; line-height: 1.22; }

  .col { position: absolute; }
  .col p { margin-bottom: 14px; }
  .col .justify { text-align: justify; }
  .rules .col-left { left: 33px; top: 6px; width: 304px; }
  .rules .col-right { left: 381px; top: 6px; width: 450px; }
  .locations .col-left { left: 33px; top: 20px; width: 304px; }
  .locations .col-right { left: 381px; top: 20px; width: 436px; }
  .locations .col p { margin-bottom: 13px; }

  .steps { list-style: none; padding-left: 51px; margin: -8px 0 10px; }
  .steps li { margin-bottom: 9px; }
  .locations .steps { padding-left: 51px; margin-top: 2px; }
  .locations .steps li { margin-bottom: 12px; }

  .alarm-photo {
    position: absolute; left: 92px; top: 214px; width: 208px; height: 116px;
    background: linear-gradient(180deg, var(--photo-light) 0%, var(--photo-dark) 100%);
  }

  .closing {
    position: absolute; top: 975px; left: 40px; width: 768px;
    text-align: center; color: var(--ink); font-size: 14.4px; line-height: 1.5;
  }

  .brand {
    position: absolute; left: 0; top: 1068px; width: 194px; height: 132px;
    background: var(--charcoal-deep);
    border-top: 4px solid var(--gold); border-right: 4px solid var(--gold);
    display: flex; flex-direction: column; align-items: center; justify-content: center; gap: 8px;
  }
  .brand .mark { width: 14px; height: 14px; background: var(--gold); }
  .brand .name { color: var(--gold); font-size: 15px; font-weight: 600; text-align: center; line-height: 1.2; }

  .call {
    position: absolute; left: 194px; top: 1054px; width: 654px;
    text-align: center; color: var(--ink); font-size: 41px; font-weight: 700;
  }

  .web-bar {
    position: absolute; left: 194px; top: 1134px; width: 654px; height: 66px;
    background: var(--gold);
    display: flex; align-items: center; justify-content: center;
    color: var(--white); font-size: 26px; font-weight: 700; letter-spacing: 3px;
  }
</style>
</head>
<body>
<main class="flyer">
  <h1 class="band-title top">Dwellings being sold, leased or an<br>existing lease is renewed</h1>
  <div class="rule"></div>

  <div class="date-bar">
    <h2 class="left">From 1 January 2017</h2>
    <h2 class="right">From 1 January 2022</h2>
  </div>

  <section class="panel rules">
    <div class="col col-left">
      <p>Requirements as for existing dwellings.</p>
      <p class="justify">Existing landlord’s and tenant’s obligations regarding the installation and testing of smoke alarms continue.</p>
      <p class="justify">Property sellers must continue to lodge a Form 24 with the Queensland Land Registry Office stating the requirements of the smoke alarm legislation have been met.</p>
    </div>
    <div class="alarm-photo" role="img" aria-label="Photo of a white photoelectric smoke alarm"></div>

    <div class="col col-right">
      <p>Smoke alarms in the dwelling must:</p>
      <ul class="steps">
        <li>i) be photoelectric (AS 3786-2014); and</li>
        <li>ii) not also contain an ionisation sensor; and</li>
        <li>iii) be less than 10 years old; and</li>
        <li>iv) operate when tested; and</li>
        <li>v) be interconnected with every other smoke alarm in the dwelling so all activate together.</li>
      </ul>
      <p>Smoke alarms must be installed on each storey:</p>
      <ul class="steps">
        <li>i) in each bedroom; and</li>
        <li>ii) in hallways which connect bedrooms and the rest of the dwelling; or</li>
        <li>iii) if there is no hallway, between the bedrooms and other parts of the storey; and</li>
        <li>iv) if there are no bedrooms on a storey at least one smoke alarm must be installed in the most likely path of travel to exit the dwelling.</li>
      </ul>
    </div>
  </section>

  <h1 class="band-title middle">Prescribed locations for installing<br>smoke alarms</h1>

  <section class="panel locations">
    <div class="col col-left">
      <p class="justify">Where practicable smoke alarms must be placed on the ceiling. Smoke alarms must not be placed:</p>
      <ul class="steps">
        <li>i) within 300mm of a corner of a<br>ceiling and a wall;</li>
        <li>ii) within 300mm of a light fitting;</li>
        <li>iii) within 400mm of an<br>air-conditioning vent;</li>
        <li>iv) within 400mm of the blades of a<br>ceiling fan.</li>
      </ul>
    </div>
    <div class="col col-right">
      <p class="justify">There are special requirements for stairways, sloping ceilings, and ceilings with exposed beams. Specific requirements will be explained in the Building Fire Safety Regulation 2008.</p>
      <p class="justify">If impractical for the prescribed location requirements to be met (e.g. may be affected by steam from shower or fumes from cooking), the owner may put the alarm at another location that will provide a warning to occupants of the dwelling.</p>
    </div>
  </section>

  <p class="closing">New legislation specifies the type, positioning and interconnectedness of alarms, which are critical<br>factors for an early warning and a quick escape. To give your family the best chance of surviving a<br>house fire, update your smoke alarms to match the new legislation as soon as you can.</p>

  <div class="brand">
    <span class="mark"></span>
    <span class="name">Tandrell Electrical</span>
  </div>

  <p class="call">Call Me on 0418362957</p>
  <div class="web-bar">www.AlarmReadyQld.com</div>
</main>
</body>
</html>
```